Webdesign für Entrümpelungsfirma
Zielgruppe
Unsere Firma heißt Tolu Hausservice und wir bieten folgende Dienstleistungen an:
Haushaltsauflösungen, Entrümpelungen, Messie-Wohnungen, Demontage-Arbeiten, Gartenpflege.
Aufgabenstellung
Unsere jetzige Seite: www.hausservice-fernwald.example
Das Logo bleibt bestehen. Es wäre schön, wenn das neue Design die Farben aufnehmen würde. Es geht erstmal nur um die Startseite.
Die Struktur soll klar und übersichtlich sein.
Wir möchten Vertrauen erwecken, aber nicht langweilig wirken. Das Design soll pfiffig sein und den Kunden aufmerksam machen.
Eine Seite, die uns sehr gut gefällt:
http://www.saubermoni.example/

```html
<!DOCTYPE html>
<html lang="de">
<head>
<meta charset="utf-8">
<title>Tolu Hausservice – Startseite</title>
<link href="https://fonts.googleapis.com/css2?family=Open+Sans:wght@300;400;600;700&display=swap" rel="stylesheet">
<style>
:root{
  --green:#8fa21d;
  --gold:#e2b417;
  --blue:#1f4f8f;
  --circle-blue:#4a6fa8;
  --text:#555;
  --heading:#444;
  --footer:#333;
  --white:#fff;
}
*{box-sizing:border-box;margin:0;padding:0}
html,body{width:1200px;height:4076px;overflow:hidden}
body{font-family:"Open Sans",Arial,sans-serif;color:var(--text);background:var(--white);position:relative}
.abs{position:absolute}
section,header,footer{position:absolute;left:0;width:1200px;overflow:hidden}
.tick{display:inline-block;width:12px;height:10px;margin-right:7px;vertical-align:middle}

.topbar{top:0;height:22px;background:var(--green);color:var(--white);font-size:11px;font-weight:700;z-index:2}
.topbar .left{left:10px;top:4px}
.topbar .right{right:10px;top:4px}

.nav{top:22px;height:60px;background:var(--white);font-size:8.5px;color:#444;overflow:visible;z-index:4}
.nav ul{list-style:none;position:absolute;top:26px;display:flex;gap:10px;white-space:nowrap}
.nav .l{right:656px}
.nav .r{left:680px}
.nav .active{border-bottom:1px solid #444;padding-bottom:3px}
.brand{position:absolute;top:-22px;left:556px;width:110px;height:119px;background:var(--white);box-shadow:0 1px 6px rgba(0,0,0,.25);display:flex;align-items:center;justify-content:center;padding-top:22px}
.brand .name{font-size:11px;font-weight:600;color:var(--heading);text-align:center;line-height:15px}

.hero{top:82px;height:505px;background:linear-gradient(180deg,#3b6f6a 0%,#6b8a5a 40%,#d9d9d6 70%,#e6e6e3 100%)}
.hero .caption{left:361px;top:347px;width:478px;height:95px;background:rgba(40,40,40,.78)}
.hero .caption p{position:absolute;left:12px;top:24px;color:var(--white);font-size:14.5px;line-height:25px}
.btn-outline{position:absolute;border:1.5px solid var(--white);border-radius:14px;color:var(--white);font-size:9px;font-weight:700;text-align:center}
.hero .btn-outline{left:291px;top:34px;width:133px;height:25px;line-height:22px}

.h2{font-weight:400;font-size:18px;color:var(--heading)}
.h2.center{width:1200px;text-align:center;left:0}
.bar{display:block;width:30px;height:2px;background:var(--gold);margin-top:12px}
.h2.light{color:var(--white)}

.allround{top:587px;height:499px}
.allround .sub{top:104px;width:1200px;text-align:center;font-size:13px;color:#555}
.allround .photo{left:234px;top:146px;width:292px;height:292px;border-radius:50%;background:radial-gradient(circle,#e6f6fa 0%,#9fdde9 100%)}
.svc{font-size:13.5px;color:#666;line-height:23px;width:240px}
.svc .tick{margin-top:-3px}

.dark-band{background:linear-gradient(90deg,#3c3a34 0%,#5b5a50 50%,#434238 100%)}
.team{top:1086px;height:293px}
.team p{left:240px;top:104px;width:340px;color:var(--white);font-size:10px;font-weight:600;line-height:17px}
.team .art{left:609px;top:85px;width:350px;height:208px;background:linear-gradient(180deg,#e8892b 0%,#9fb330 60%,#384c7a 100%);border-radius:40px 40px 0 0}

.haushalt{top:1379px;height:513px}
.haushalt .sub{top:104px;font-size:13px;text-align:center;width:1200px}
.col h3{font-size:13.5px;font-weight:400;color:#444;margin-bottom:10px}
.col p{font-size:10px;line-height:15.5px;color:#555}
.col .ico{position:absolute;left:-36px;top:0;width:22px;height:22px}
.haushalt .note{width:1200px;text-align:center;font-size:10px;font-weight:700;color:#444;line-height:15px}
.green{color:var(--green)}
.btn-blue-outline{position:absolute;left:546px;top:454px;width:108px;height:25px;border:1.5px solid var(--blue);border-radius:13px;color:var(--blue);font-size:9px;font-weight:700;text-align:center;line-height:22px}

.messie{top:1892px;height:226px;background:linear-gradient(90deg,#2e2b29 0%,#5b534b 50%,#3a3532 100%)}
.messie .art{left:285px;top:47px;width:139px;height:179px;background:linear-gradient(180deg,#c9b8a8 0%,#9a9aa0 100%);border-radius:60px 60px 0 0}
.messie p{left:486px;top:145px;color:var(--white);font-size:12.5px}

.preise{top:2118px;height:334px}
.preise p{left:240px;top:120px;width:470px;font-size:10px;line-height:17px}
.preise .art{left:731px;top:50px;width:228px;height:228px;border-radius:50%;background:var(--circle-blue)}

.wert{top:2452px;height:288px;background:linear-gradient(90deg,#3a2318 0%,#6b4330 50%,#3d261b 100%)}
.wert .art{left:245px;top:65px;width:277px;height:166px;background:linear-gradient(180deg,#9a5a2c 0%,#cfc7b8 60%,#e8e2d6 100%);border-radius:6px}
.wert p{left:548px;top:106px;width:420px;color:var(--white);font-size:10px;line-height:16.5px}

.garten{top:2740px;height:300px}
.garten .art{left:240px;top:70px;width:227px;height:158px;background:linear-gradient(135deg,#b48a4c 0%,#6aa33a 60%,#d8d8d8 100%);border-radius:8px}
.garten .sub{left:486px;top:116px;font-size:12px}
.garten ul{list-style:none;position:absolute;font-size:10px;line-height:19.5px;width:235px}
.garten ul li .tick{width:9px;height:8px;margin-right:6px}

.moebel{top:3040px;height:257px;background:linear-gradient(90deg,#3d3b38 0%,#66625b 55%,#4a4843 100%)}
.moebel p{left:240px;top:131px;width:400px;color:var(--white);font-size:10px;line-height:16.5px}
.moebel .art{left:708px;top:55px;width:215px;height:158px;background:linear-gradient(160deg,#d9b089 0%,#b9875d 100%);border-radius:4px}
.totop{position:absolute;left:1163px;top:205px;width:27px;height:24px;background:#333;border-radius:3px}

.contact{top:3297px;height:338px}
.contact .company{left:240px;top:114px;font-size:10px;font-weight:700;color:#444}
.contact .details{left:240px;top:150px;font-size:10px;line-height:19.5px;color:#555;list-style:none}
.contact .details svg{width:10px;height:10px;margin-right:8px;vertical-align:-1px}
.field{position:absolute;border:1px solid #ddd;width:226px;height:32px;padding:3px 6px;font-size:6px;color:#999}
.field b{display:block;font-weight:600;color:#777;margin-bottom:4px}
.field.area{width:473px;height:89px}
.send{position:absolute;left:486px;top:290px;width:54px;height:24px;background:var(--blue);color:var(--white);font-size:8px;font-weight:700;text-align:center;line-height:24px;border-radius:2px}

.map{top:3635px;height:378px;background:linear-gradient(135deg,#eae6de 0%,#e3e1da 50%,#ecebe5 100%)}

footer{top:4013px;height:63px;background:var(--footer);color:#999;font-size:9.5px;text-align:center;line-height:63px}
footer strong{color:var(--white);font-weight:700}
</style>
</head>
<body>

<svg width="0" height="0" style="position:absolute">
  <defs>
    <symbol id="tick" viewBox="0 0 12 10"><path d="M1 5.5 L4.5 9 L11 1.5" fill="none" stroke="#8fa21d" stroke-width="2.4"/></symbol>
  </defs>
</svg>

<header class="topbar">
  <span class="abs left">✎ Angebot anfordern</span>
  <span class="abs right">✆ Hotline: 07531 482915</span>
</header>

<header class="nav">
  <ul class="l"><li>Team</li><li>Haushaltsauflösungen &amp; Entrümpelungen</li><li>Messie Wohnung</li><li>Preise</li></ul>
  <div class="brand"><span class="name">Tolu<br>Hausservice</span></div>
  <ul class="r"><li>Wertanrechnung – Ihr Vorteil</li><li>Gartenpflege</li><li>Möbel-Montage</li><li class="active">Kontakt</li></ul>
</header>

<section class="hero" role="img" aria-label="Foto: drei lächelnde Mitarbeiter in weißen Firmen-T-Shirts vor einer Landschaft">
  <div class="abs caption">
    <p>Tolu Hausservice: Ihr starker<br>Partner rund um's Haus</p>
    <span class="btn-outline">Jetzt Angebot anfordern</span>
  </div>
</section>

<section class="allround">
  <h2 class="abs h2 center" style="top:50px">Allround-Service</h2>
  <p class="abs sub">Wir bieten Ihnen einen Rundum-Service für Ihre Liegenschaft an:</p>
  <div class="abs photo" role="img" aria-label="Illustration: Werkzeuge, Schubkarre und Gartengeräte im Kreis"></div>
  <div class="abs svc" style="left:549px;top:170px"><svg class="tick"><use href="#tick"/></svg>Hauswartstätigkeiten</div>
  <div class="abs svc" style="left:549px;top:215px"><svg class="tick"><use href="#tick"/></svg>Gartenpflege</div>
  <div class="abs svc" style="left:549px;top:259px"><svg class="tick"><use href="#tick"/></svg>Putzservice: Haushaltsreinigung, Endreinigung, Baustellen-Reinigung, Gebäude-Reinigung</div>
  <div class="abs svc" style="left:549px;top:352px"><svg class="tick"><use href="#tick"/></svg>Reparaturen aller Art</div>
  <div class="abs svc" style="left:549px;top:396px"><svg class="tick"><use href="#tick"/></svg>Renovierungen</div>
  <div class="abs svc" style="left:795px;top:175px;width:170px"><svg class="tick"><use href="#tick"/></svg>Demontage-Arbeiten und Möbel-Montage</div>
  <div class="abs svc" style="left:795px;top:246px"><svg class="tick"><use href="#tick"/></svg>Haushaltsauflösungen</div>
  <div class="abs svc" style="left:795px;top:295px"><svg class="tick"><use href="#tick"/></svg>Entrümpelungen</div>
  <div class="abs svc" style="left:795px;top:344px"><svg class="tick"><use href="#tick"/></svg>Messie-Wohnungen</div>
  <div class="abs svc" style="left:795px;top:394px"><svg class="tick"><use href="#tick"/></svg>Senioren-Umzüge</div>
</section>

<section class="team dark-band">
  <h2 class="abs h2 light" style="left:240px;top:50px">Unser Team<span class="bar"></span></h2>
  <p class="abs">Wir sind ein gut eingespieltes Familien-Unternehmen mit bärenstarken, freundlichen Männern und Frauen.<br>Unser Team bietet Ihnen einen Komplett-Service rund um Haushaltsauflösungen, Entrümpelungen, Hauswarts-Tätigkeiten, Gebäudereinigung, Baustellen-Reinigung und Renovierung an.<br>Unsere Mitarbeiter haben eine langjährige Erfahrung und erledigen alle anfallenden Tätigkeiten schnell, gründlich und kompetent.</p>
  <div class="abs art" role="img" aria-label="Illustration: vier gezeichnete Teammitglieder in Arbeitskleidung"></div>
</section>

<section class="haushalt">
  <h2 class="abs h2 center" style="top:49px">Haushaltsauflösungen Entrümpelungen</h2>
  <p class="abs sub">Von den Profis, schnell, preiswert und diskret.</p>
  <div class="abs col" style="left:277px;top:148px;width:360px">
    <svg class="ico" viewBox="0 0 22 22"><path d="M3 20 L14 9" stroke="#8fa21d" stroke-width="3"/><path d="M16 2 l1 3 3 1 -3 1 -1 3 -1-3 -3-1 3-1z" fill="#8fa21d"/></svg>
    <h3>Wir lösen auf</h3>
    <p>Wohnungen, Häuser, Studentenzimmer, Senioren-Wohnungen, Messi-Wohnungen, Keller, Garagen, Werkstätten und auch ganze Gebäude.<br>Wir sind schnell, stark, gründlich und zuverlässig. Wir arbeiten umsichtig und mit äußerster Diskretion.<br>Bei uns bekommen Sie sehr gute Qualität zu fairen Preisen!<br>Wenn wir gehen ist alles leer und besenrein.</p>
  </div>
  <div class="abs col" style="left:710px;top:148px;width:290px">
    <svg class="ico" viewBox="0 0 22 22"><path d="M2 10h4v10H2z M8 10 L12 2 c2 0 3 1 2 4 L13 9h6c2 0 2 2 1 3 l-2 7H8z" fill="#8fa21d"/></svg>
    <h3>Ihre Vorteile bei uns:</h3>
    <p>Komplette Abwicklung aus einer Hand.<br>Gratis Besenreinigung.<br>Haftpflichtversicherung für alle Mitarbeiter.<br>Wert-Anrechnung und preiswerte Entsorgung.<br>Kurzfristige Termine sind möglich!<br>Der Müll wird fachgerecht entsorgt.</p>
  </div>
  <p class="abs note" style="top:294px">Gerne besichtigen wir Ihre Räumlichkeiten und erstellen Ihnen ein kostenloses und unverbindliches  Angebot inklusive Wertermittlung und-<br>Anrechnung.</p>
  <p class="abs note" style="top:343px">Bei uns gibt es einen garantierten Festpreis ohne versteckte Kosten.</p>
  <p class="abs note" style="top:371px">Wir beraten Sie kompetent und ausführlich!</p>
  <p class="abs note" style="top:401px">Rufen Sie uns jetzt an! <span class="green">07531 482 915</span> oder in der Schweiz: <span class="green">+41 71 5550142</span></p>
  <span class="btn-blue-outline">Angebot anfordern</span>
</section>

<section class="messie">
  <div class="abs art" role="img" aria-label="Foto: erschrockene Frau hält sich die Hände an den Kopf"></div>
  <h2 class="abs h2 light" style="left:486px;top:88px">Messie-Wohnung?<span class="bar"></span></h2>
  <p class="abs">Wir entrümpeln jede Messie-Wohnung gründlich, schnell und diskret.</p>
</section>

<section class="preise">
  <h2 class="abs h2" style="left:240px;top:62px">Preise<span class="bar"></span></h2>
  <p class="abs">Bei jeder Haushaltsauflösung oder Räumung kommen verschiedene Faktoren zusammen:<br>Wie viel gibt es zu räumen? Soll eine Küche demontiert werden? Sind Möbel und Gebrauchsgegenstände noch zu verwerten oder müssen sie entsorgt werden? Gibt es einen Keller, Garage oder einen Schuppen?<br>Wie viel Arbeit möchten oder können Sie selbst investieren?<br>Einen Haushalt aufzulösen ist oft umfangreich und viele wissen nicht, welche Kosten anfallen werden.<br>Wir beraten Sie sehr gerne bei einem Gespräch am Telefon und bei einem kostenlosen Besichtigungstermin vor Ort. Rufen Sie uns bitte an!<br>Tel. <span class="green" style="font-weight:700">+49 7531 482 915</span></p>
  <div class="abs art" role="img" aria-label="Illustration: Handschlag zweier Geschäftspartner auf blauem Kreis"></div>
</section>

<section class="wert">
  <div class="abs art" role="img" aria-label="Foto: Frisierkommode aus Holz und helles Sofa"></div>
  <h2 class="abs h2 light" style="left:548px;top:53px">Wertanrechnung – Ihr Vorteil<span class="bar"></span></h2>
  <p class="abs">Warum soll man gute, noch verwertbare Möbel und Gebrauchsgegenstände fortwerfen?<br>Möbel sowie Gebrauchsgegenstände, die gut erhalten sind, werden von uns nicht auf der Mülldeponie entsorgt!<br>Vereinbaren Sie mit uns einen kostenlosen Besichtigungstermin, um die Kosten für Ihre Räumung sowie eine mögliche Wertanrechnung einzuschätzen.<br>Rufen Sie uns noch heute an: <span class="green">07531 482 915</span><br>Oder schreiben Sie uns eine E-Mail: <span class="green" style="font-weight:700">info@tolu-hausservice.example</span></p>
</section>

<section class="garten">
  <div class="abs art" role="img" aria-label="Foto: Korb mit Gartenwerkzeug, Gießkanne und Topfpflanze"></div>
  <h2 class="abs h2" style="left:486px;top:62px">Gartenpflege<span class="bar"></span></h2>
  <p class="abs sub">Ihr Garten soll schön und gepflegt aussehen! Wir bieten an:</p>
  <ul style="left:486px;top:139px">
    <li><svg class="tick"><use href="#tick"/></svg>Die Pflege von Hecken, Sträuchern und Bäumen</li>
    <li><svg class="tick"><use href="#tick"/></svg>Rasenmähen</li>
    <li><svg class="tick"><use href="#tick"/></svg>Laub rechen</li>
    <li><svg class="tick"><use href="#tick"/></svg>Unkraut jähten</li>
    <li><svg class="tick"><use href="#tick"/></svg>Abfälle einsammeln</li>
  </ul>
  <ul style="left:733px;top:139px">
    <li><svg class="tick"><use href="#tick"/></svg>Pflege der Blumenbeete</li>
    <li><svg class="tick"><use href="#tick"/></svg>Zäune setzen und pflegen</li>
    <li><svg class="tick"><use href="#tick"/></svg>Gartengestaltung</li>
    <li><svg class="tick"><use href="#tick"/></svg>Bepflanzungen</li>
    <li><svg class="tick"><use href="#tick"/></svg>Fragen Sie nach unseren günstigen Preisen!</li>
  </ul>
</section>

<section class="moebel">
  <h2 class="abs h2 light" style="left:240px;top:69px">Möbel-Montage<span class="bar"></span></h2>
  <p class="abs">Sie haben sich ein neues Möbelstück gekauft? Sie haben keine Zeit, es selbst zu montieren? Oder Sie wissen einfach nicht, wo hinten und vorne ist?<br>Kein Problem! Vom einfach Nordhus-Regal bis zum komplizierten Massivholzschrank können wir alles montieren oder auch demontieren!</p>
  <div class="abs art" role="img" aria-label="Foto: gestapelte Umzugskartons"></div>
  <span class="totop"><svg viewBox="0 0 27 24" width="27" height="24"><path d="M9 14 L13.5 9 L18 14" fill="none" stroke="#fff" stroke-width="1.6"/></svg></span>
</section>

<section class="contact">
  <h2 class="abs h2" style="left:240px;top:40px">Kontaktdaten<span class="bar"></span></h2>
  <h2 class="abs h2" style="left:486px;top:40px">Kontaktformular / Angebot anfordern</h2>
  <p class="abs company">Welbrand GmbH</p>
  <ul class="abs details">
    <li><svg viewBox="0 0 10 10"><path d="M5 0a3.5 3.5 0 0 1 3.5 3.5C8.5 6 5 10 5 10S1.5 6 1.5 3.5A3.5 3.5 0 0 1 5 0z" fill="#8fa21d"/></svg>Lindenweg 12</li>
    <li>35463 Fernwald</li>
    <li><svg viewBox="0 0 10 10"><path d="M2 0l2 2.5-1 1.5c.8 1.5 1.5 2.2 3 3l1.5-1L10 8 8.5 10C4 9 1 6 0 1.5z" fill="#8fa21d"/></svg>07531 482 915</li>
    <li><svg viewBox="0 0 10 10"><path d="M2 0l2 2.5-1 1.5c.8 1.5 1.5 2.2 3 3l1.5-1L10 8 8.5 10C4 9 1 6 0 1.5z" fill="#8fa21d"/></svg>07531 482 916</li>
    <li><svg viewBox="0 0 10 10"><rect x="0" y="2" width="10" height="7" fill="#8fa21d"/><path d="M0 2l5 4 5-4" fill="none" stroke="#fff"/></svg>info@tolu-hausservice.example</li>
    <li><svg viewBox="0 0 10 10"><rect x="0.5" y="1" width="9" height="6" fill="none" stroke="#8fa21d"/><path d="M3 9h4" stroke="#8fa21d"/></svg>www.hausservice-fernwald.example</li>
  </ul>
  <div class="field" style="left:486px;top:95px"><b>NAME*</b>Geben Sie bitte Ihren Namen ein</div>
  <div class="field" style="left:733px;top:95px"><b>E-MAIL*</b>Geben Sie bitte Ihre E-Mail-Adresse ein</div>
  <div class="field" style="left:486px;top:138px"><b>TELEFON</b>Geben Sie bitte Ihre Telefonnummer ein</div>
  <div class="field" style="left:733px;top:138px"><b>BETREFF*</b>Geben Sie bitte den Betreff ein</div>
  <div class="field area" style="left:486px;top:179px"><b>NACHRICHT*</b>Geben Sie bitte Ihre Nachricht ein</div>
  <span class="send">Senden</span>
</section>

<section class="map" role="img" aria-label="Stadtplan mit Standortmarkierung des Firmensitzes"></section>

<footer>© 2016 Hausservice Fernwald, Haushaltsauflösungen, Hausmeister, Entrümpelungen. | <strong>Impressum</strong></footer>

</body>
</html>
```